Business Card Design

I am a realtor and i also flip houses. I am CEO and Founder of my business which is Halvorsen Group LLC which is named after my great uncle who died and i was really close to. He was a wonderful friendly man so i want my business to represent him too. My business works with a lot of different people but i want mainly something to show i am a strong confidant woman who owns there own business. I have a really fun personality so i don't want anything TOO serious or manly. I want the perfect mix. My last two business cards i created are too embarrassing to hand out because they are far too girly and i deal with a lot of millionaire clients. I live out in the Palm Springs California area. I think its very important to show i am a single mom, female with her own business at only 24. I don't want to just be a female that blends in with all of the other serious people but yet i don't want to seem immature. People are telling me to stay away from pinks and purples but i don't want blues and greens because they represent men more. But i won't say no to them if there is a happy medium.

Industry/Entity Type

Realtor

Contact Information for Business Card

Halvorsen Group, LLC
Corinne Pell
27318 Quillan Ave, B1 582
Verdell Palms, CA 92418
760-555-0147
Corinnetpell@mailverta.com

```html
<!DOCTYPE html>
<html lang="en">
<head>
<meta charset="utf-8">
<title>Halvorsen Group, LLC — Business Card</title>
<link rel="stylesheet" href="https://fonts.googleapis.com/css2?family=Ubuntu:wght@500&family=Open+Sans:wght@400&family=Dancing+Script:wght@700&display=swap">
<style>
  :root {
    --stage: #2a2a2c;
    --card-black: #050506;
    --panel-black: #0b0b0d;
    --mesh-dark: #0d1a1d;
    --mesh-light: #1f3a40;
    --violet: #7b63d6;
    --ink-white: #e9e9ee;
    --ink-gray: #56565a;
    --paper-light: #f4f4f4;
    --paper-mid: #b9b9bb;
    --edge-dark: #111214;
  }
  * { box-sizing: border-box; margin: 0; padding: 0; }
  html, body { width: 1200px; height: 800px; overflow: hidden; }
  body {
    background: var(--stage);
    display: flex;
    align-items: center;
    justify-content: center;
    gap: 48px;
    font-family: "Open Sans", sans-serif;
  }
  .card {
    position: relative;
    width: 525px;
    height: 300px;
    overflow: hidden;
    box-shadow: 0 18px 40px rgba(0,0,0,.55);
  }

  /* Front */
  .card-front { background: var(--card-black); }
  .mesh-band {
    position: absolute;
    left: 0; right: 0; top: 70px; height: 160px;
    background: radial-gradient(ellipse at 50% 50%, var(--mesh-light) 0%, var(--mesh-dark) 60%, var(--card-black) 100%);
  }
  .logo-panel {
    position: absolute;
    left: 28px; top: 40px;
    width: 225px; height: 150px;
    background: var(--panel-black);
    display: flex; flex-direction: column; justify-content: center;
    padding-left: 18px;
  }
  .contact-panel {
    position: absolute;
    right: 28px; bottom: 22px;
    width: 232px; height: 140px;
    background: var(--panel-black);
    padding: 12px 14px;
  }
  .wordmark {
    font-family: "Ubuntu", sans-serif;
    font-weight: 500;
    line-height: 1;
  }
  .wordmark .name-line { display: block; color: var(--violet); }
  .wordmark .group-line { display: block; letter-spacing: .32em; }
  .logo-panel .wordmark .name-line { font-size: 32px; }
  .logo-panel .wordmark .group-line { font-size: 14px; margin-top: 6px; color: var(--ink-white); }

  .agent-name {
    font-family: "Dancing Script", cursive;
    font-weight: 700;
    font-size: 28px;
    color: var(--violet);
    margin-bottom: 6px;
    white-space: nowrap;
  }
  .contact-list { list-style: none; color: var(--ink-white); font-size: 10.5px; line-height: 1.5; }
  .contact-list li { display: flex; align-items: flex-start; gap: 7px; white-space: nowrap; }
  .contact-list svg { width: 10px; height: 10px; margin-top: 3px; flex: none; }
  .contact-list .no-icon { padding-left: 17px; }

  /* Back */
  .card-back { background: var(--edge-dark); }
  .card-back .face { position: absolute; inset: 0; width: 100%; height: 100%; }
  .back-logo {
    position: absolute; inset: 0;
    display: flex; flex-direction: column; align-items: center; justify-content: center;
  }
  .back-logo .wordmark .name-line { font-size: 64px; }
  .back-logo .wordmark .group-line { font-size: 26px; margin-top: 8px; color: var(--ink-gray); }
</style>
</head>
<body>

  <section class="card card-front" aria-label="Business card front">
    <div class="mesh-band" role="img" aria-label="Dark teal woven mesh texture band"></div>
    <div class="logo-panel">
      <div class="wordmark">
        <span class="name-line">Halvorsen</span>
        <span class="group-line">GROUP, LLC</span>
      </div>
    </div>
    <div class="contact-panel">
      <p class="agent-name">Corinne Pell</p>
      <ul class="contact-list">
        <li>
          <svg viewBox="0 0 10 10" aria-hidden="true"><rect x="2" y="0.5" width="6" height="9" rx="1" fill="none" stroke="currentColor"/></svg>
          760-555-0147
        </li>
        <li>
          <svg viewBox="0 0 10 10" aria-hidden="true"><rect x="0.5" y="2" width="9" height="6" fill="none" stroke="currentColor"/><path d="M0.5 2 L5 5.5 L9.5 2" fill="none" stroke="currentColor"/></svg>
          Corinnetpell@mailverta.com
        </li>
        <li>
          <svg viewBox="0 0 10 10" aria-hidden="true"><path d="M5 9.5 C2 6 1.5 5 1.5 3.8 A3.5 3.5 0 0 1 8.5 3.8 C8.5 5 8 6 5 9.5Z" fill="none" stroke="currentColor"/><circle cx="5" cy="3.8" r="1.2" fill="currentColor"/></svg>
          27318 Quillan Ave, B1 582
        </li>
        <li class="no-icon">Verdell Palms, CA 92418</li>
      </ul>
    </div>
  </section>

  <section class="card card-back" aria-label="Business card back">
    <svg class="face" viewBox="0 0 525 300" aria-hidden="true">
      <defs>
        <radialGradient id="paper-glow" cx="50%" cy="40%" r="65%">
          <stop offset="0%" stop-color="#f4f4f4"/>
          <stop offset="100%" stop-color="#b9b9bb"/>
        </radialGradient>
      </defs>
      <polygon points="22,0 503,0 503,22 525,40 525,260 503,278 503,300 22,300 22,278 0,260 0,40 22,22" fill="url(#paper-glow)"/>
    </svg>
    <div class="back-logo">
      <div class="wordmark">
        <span class="name-line">Halvorsen</span>
        <span class="group-line">GROUP, LLC</span>
      </div>
    </div>
  </section>

</body>
</html>
```